Velvet Crest Car Detailing Brochure

I would like a trifold brochure designed for my car detailing business. The background has to be full black or mostly black with some designing using only colors present in our logo.

Front page must have our logo and name, list of services, a photo and mybe our phone number but no long text.

Inside I want to present each service one by one with its description and a photo representing/showing each service. (I will provide the text below). For photos, use stock photos and I will add come of mines already too.

On the back of the brochure I want to have contact & info: phone number, opening hours, address, website, Instagram.

Outside left I want the text About us and photo/design.

I want the brochure to be neat, professional, easy to read, but at the same time not too boring.

Text:
1. About us
a. the ultimate destination for car care in Geneva. We provide personalized, detail-oriented services that bring out the best in your car. With our expert techniques and dedicated approach, we ensure that your car receives the utmost care and attention. Experience a place where passion meets precision and let us create an exceptional car care experience designed just for you.
2. Services:

DETAILING & HAND WASH

• Comprehensive exterior & interior care
• Personalisation and tailored cleaning packages
• Decontamination
• Premium products
• Attention to detail for a perfect finish

POLISHING

• Eliminates scratches, holograms
• Revives and protects paint
• Ensures lasting gloss
• Enhances paint life
• Preserves car’s value and beauty

CERAMIC TREATMENT

• Durable paint protection
• Water-repellent (hydrophobic) effect
• Easier cleaning, enhanced shine
• Long-term surface safeguarding
• Shields against environmental impacts

DRY ICE WASH

• Innovative, waterless method
• Safe for all car parts
• Deep cleans, removes odors
• Allergen-free, antibacterial
• Gentle, effective
• Advanced cleaning technology

COVERING

• Personalized vehicle styling
• More than 150 colours available
• Clean cut without using a cutter
• High-quality, durable materials
• Custom designs available

PROTECTION FILM

• Invisible, durable shield
• Self-healing technology
• 10-year warranty by QR VONT

DETAILING BOUTIQUE

• Premium brands available
• Buy on site during your visit
• Marble Harbour, Zeb Autos, DRUP Polaro
• Essential for at-home car care
• Perfect for quick touch-ups
(for these three brands you can put their logos

Target Market(s)

Our target market includes car owners of all price ranges, with a special focus on those who are passionate about their vehicles. We cater to clients who value excellent service and results, and seek to maintain their cars in pristine condition.

Industry/Entity Type

Automobile / Car detailing

Colors

Designer to choose colors to be used in the design.

Requirements
Must have
• Brand Consistency: The brochure must adhere to our brand colors and style, particularly utilizing the colors present in our logo. Trifold Layout: The design must be specifically tailored for a trifold brochure format. Legibility: Text must be easy to read against the mostly black background, with appropriate font size and style. Professional Look and Feel: The overall design must convey professionalism while being engaging and not overly complex. Photo representation: each service description should have a phot presenting it.
Should not have
• Overcrowded Design: Avoid cluttering with too much text or too many images. The layout should be clean and easy to navigate. Cartoonish Fonts or Graphics: Avoid using unprofessional or casual fonts and graphics that do not align with the upscale and professional image of our business. Distracting Backgrounds: The background should complement and not overpower the content. Stick to the theme of mostly black with design elements from our logo.

```html
<!DOCTYPE html>
<html lang="en">
<head>
<meta charset="utf-8">
<title>Velvet Crest Car Detailing – Trifold Brochure</title>
<link rel="stylesheet" href="https://fonts.googleapis.com/css2?family=Montserrat:wght@400;500;600;700;800&display=swap">
<style>
  :root{
    --stage:#d6d6d8;
    --ink:#0b0b0d;
    --panel:#121216;
    --line:#2a2a31;
    --text:#f1f1f4;
    --muted:#b9b9c4;
    --magenta:#e3197e;
    --violet:#8a3fd1;
    --blue:#3d8fe0;
    --brand-grad:linear-gradient(90deg,var(--blue),var(--violet) 50%,var(--magenta));
  }
  *{box-sizing:border-box;margin:0;padding:0}
  html,body{width:804px;height:1200px;overflow:hidden}
  body{background:var(--stage);font-family:"Montserrat",sans-serif;color:var(--text)}
  .spread{position:absolute;left:22px;width:760px;height:560px;background:var(--ink);display:flex;box-shadow:0 6px 18px rgba(0,0,0,.28);overflow:hidden}
  .spread--outside{top:26px}
  .spread--inside{top:614px}
  .panel{position:relative;width:253.33px;height:100%;padding:22px 18px;border-right:1px dashed var(--line);overflow:hidden}
  .panel:last-child{border-right:none}
  .swoosh{position:absolute;pointer-events:none}
  .photo{border-radius:6px;position:relative}
  .photo--polish{background:radial-gradient(circle at 40% 45%,#6a6f7d,#2b2e36 60%,#16171c)}
  .photo--car{background:radial-gradient(circle at 60% 40%,#5a5f6a,#262830 60%,#121317)}
  .photo--bottle{background:radial-gradient(circle at 50% 50%,#8b5a2b,#3a2a1c 55%,#141416)}
  .photo--interior{background:radial-gradient(circle at 35% 55%,#9aa1ad,#3b3f48 55%,#15161a)}
  .section-title{font-weight:800;font-size:15px;letter-spacing:.08em;text-transform:uppercase;display:inline-block;padding:5px 12px;border-radius:3px;background:var(--brand-grad)}
  .tick-list{list-style:none}
  .tick-list li{font-size:8.4px;font-weight:600;letter-spacing:.06em;text-transform:uppercase;display:flex;align-items:center;gap:7px;padding:4px 0;border-bottom:1px solid var(--line)}
  .tick{width:11px;height:11px;border-radius:50%;background:var(--magenta);display:inline-flex;align-items:center;justify-content:center;flex:none}
  .contact-row{display:flex;gap:8px;align-items:flex-start;font-size:8.5px;line-height:1.4;margin-bottom:9px;color:var(--text)}
  .contact-icon{width:18px;height:18px;border-radius:50%;background:var(--violet);display:inline-flex;align-items:center;justify-content:center;flex:none}
  .brand{display:flex;align-items:center;gap:8px}
  .brand-dot{width:34px;height:34px;border-radius:50%;border:2px solid var(--magenta);flex:none}
  .brand-name{font-weight:700;font-size:11px;letter-spacing:.05em;text-transform:uppercase;color:var(--text);line-height:1.2}
  .headline{font-weight:800;font-size:17px;line-height:1.2;text-transform:uppercase}
  .headline .accent{color:var(--magenta)}
  .web{font-size:9px;font-weight:600;letter-spacing:.06em;color:var(--muted)}
  .about-text{font-size:8.6px;line-height:1.55;color:var(--muted);margin-top:10px}
  .service{display:flex;gap:9px;margin-top:11px}
  .service .photo{width:52px;height:52px;border-radius:50%;flex:none;border:2px solid var(--violet)}
  .service-title{font-size:9px;font-weight:800;letter-spacing:.06em;text-transform:uppercase;color:var(--magenta);margin-bottom:3px}
  .service ul{list-style:none}
  .service li{font-size:7.4px;line-height:1.45;color:var(--text)}
  .service li::before{content:"•";color:var(--blue);margin-right:4px}
  .panel-heading{font-weight:800;font-size:15px;letter-spacing:.08em;text-transform:uppercase}
  .underline{height:3px;width:48px;background:var(--brand-grad);margin-top:5px;border-radius:2px}
</style>
</head>
<body>

<!-- Outside spread -->
<section class="spread spread--outside">
  <article class="panel panel--services-list">
    <svg class="swoosh" style="left:0;bottom:0" width="254" height="140" viewBox="0 0 254 140"><path d="M0 140 C60 70 160 120 254 40 L254 140Z" fill="var(--violet)" opacity=".35"/><path d="M0 140 C80 100 170 135 254 90 L254 140Z" fill="var(--magenta)" opacity=".55"/></svg>
    <div class="photo photo--polish" style="height:170px" role="img" aria-label="Technician polishing a car panel with a rotary polisher"></div>
    <ul class="tick-list" style="margin-top:16px">
      <li><span class="tick"><svg width="7" height="7" viewBox="0 0 10 10"><path d="M2 5l2 2 4-4" stroke="#fff" stroke-width="1.8" fill="none"/></svg></span>Detailing &amp; hand wash</li>
      <li><span class="tick"><svg width="7" height="7" viewBox="0 0 10 10"><path d="M2 5l2 2 4-4" stroke="#fff" stroke-width="1.8" fill="none"/></svg></span>Polishing</li>
      <li><span class="tick"><svg width="7" height="7" viewBox="0 0 10 10"><path d="M2 5l2 2 4-4" stroke="#fff" stroke-width="1.8" fill="none"/></svg></span>Ceramic treatment</li>
      <li><span class="tick"><svg width="7" height="7" viewBox="0 0 10 10"><path d="M2 5l2 2 4-4" stroke="#fff" stroke-width="1.8" fill="none"/></svg></span>Dry ice wash</li>
      <li><span class="tick"><svg width="7" height="7" viewBox="0 0 10 10"><path d="M2 5l2 2 4-4" stroke="#fff" stroke-width="1.8" fill="none"/></svg></span>Covering</li>
      <li><span class="tick"><svg width="7" height="7" viewBox="0 0 10 10"><path d="M2 5l2 2 4-4" stroke="#fff" stroke-width="1.8" fill="none"/></svg></span>Protection film</li>
      <li><span class="tick"><svg width="7" height="7" viewBox="0 0 10 10"><path d="M2 5l2 2 4-4" stroke="#fff" stroke-width="1.8" fill="none"/></svg></span>Detailing boutique</li>
    </ul>
  </article>

  <article class="panel panel--contact">
    <div class="photo photo--bottle" style="height:190px" role="img" aria-label="Detailing product bottle and applicator pad on a car seat"></div>
    <div style="margin-top:20px">
      <h2 class="panel-heading">Contact</h2>
      <div class="underline"></div>
    </div>
    <div style="margin-top:16px">
      <div class="contact-row"><span class="contact-icon"><svg width="9" height="9" viewBox="0 0 10 10"><path d="M2 1l2 2-1 1c.6 1.3 1.7 2.4 3 3l1-1 2 2-1.5 1.5C4.5 9 1 5.5.5 2.5Z" fill="#fff"/></svg></span><span>+41 22 555 01 48</span></div>
      <div class="contact-row"><span class="contact-icon"><svg width="9" height="9" viewBox="0 0 10 10"><rect x="1" y="2.5" width="8" height="5.5" fill="none" stroke="#fff"/><path d="M1 2.5l4 3 4-3" fill="none" stroke="#fff"/></svg></span><span>hello@velvetcrest.ch</span></div>
      <div class="contact-row"><span class="contact-icon"><svg width="9" height="9" viewBox="0 0 10 10"><path d="M5 .5a3 3 0 0 1 3 3c0 2.3-3 6-3 6s-3-3.7-3-6a3 3 0 0 1 3-3Z" fill="#fff"/><circle cx="5" cy="3.5" r="1" fill="var(--violet)"/></svg></span><span>Rue des Lilas 12<br>1205 Genève</span></div>
      <div class="contact-row"><span class="contact-icon"><svg width="9" height="9" viewBox="0 0 10 10"><circle cx="5" cy="5" r="4" fill="none" stroke="#fff"/><path d="M5 2.5V5l1.8 1.2" stroke="#fff" fill="none"/></svg></span><span>Mon – Fri: 8:00 – 18:30<br>Sat: 9:00 – 16:00</span></div>
      <div class="contact-row"><span class="contact-icon"><svg width="9" height="9" viewBox="0 0 10 10"><rect x="1.5" y="1.5" width="7" height="7" rx="2" fill="none" stroke="#fff"/><circle cx="5" cy="5" r="1.6" fill="none" stroke="#fff"/></svg></span><span>@velvetcrest.detailing</span></div>
      <div class="contact-row"><span class="contact-icon"><svg width="9" height="9" viewBox="0 0 10 10"><circle cx="5" cy="5" r="4" fill="none" stroke="#fff"/><path d="M1 5h8M5 1c2 2.5 2 5.5 0 8M5 1c-2 2.5-2 5.5 0 8" stroke="#fff" fill="none" stroke-width=".8"/></svg></span><span>www.velvetcrest.ch</span></div>
    </div>
  </article>

  <article class="panel panel--cover">
    <svg class="swoosh" style="left:0;top:0" width="254" height="560" viewBox="0 0 254 560"><path d="M254 120 C160 200 210 330 254 380Z" fill="var(--magenta)" opacity=".7"/><path d="M254 150 C190 220 220 320 254 350Z" fill="var(--blue)" opacity=".6"/></svg>
    <div class="brand" style="justify-content:flex-end">
      <span class="brand-dot"></span>
      <span class="brand-name">Velvet Crest<br>Car Detailing</span>
    </div>
    <div class="photo photo--interior" style="height:230px;margin-top:22px;border-radius:50% 6px 6px 6px/30% 6px 6px 6px" role="img" aria-label="Detailer cleaning a car interior with a dry ice blaster"></div>
    <p class="headline" style="margin-top:26px;text-align:right">The ultimate<br>destination for<br><span class="accent">luxury car care</span><br>in Geneva</p>
    <div style="height:3px;background:var(--brand-grad);margin:14px 0 10px auto;width:90px;border-radius:2px"></div>
    <p class="web" style="text-align:right">www.velvetcrest.ch</p>
  </article>
</section>

<!-- Inside spread -->
<section class="spread spread--inside">
  <article class="panel panel--about">
    <h2 class="section-title">About us</h2>
    <p class="about-text">The ultimate destination for car care in Geneva. We provide personalized, detail-oriented services that bring out the best in your car. With our expert techniques and dedicated approach, we ensure that your car receives the utmost care and attention. Experience a place where passion meets precision and let us create an exceptional car care experience designed just for you.</p>
    <div class="photo photo--car" style="height:110px;margin-top:14px" role="img" aria-label="Freshly detailed black car in the workshop"></div>
    <div class="service">
      <div class="photo photo--interior" role="img" aria-label="Hand washing a car body with foam"></div>
      <div><h3 class="service-title">Detailing &amp; hand wash</h3>
        <ul><li>Comprehensive exterior &amp; interior care</li><li>Personalisation and tailored cleaning packages</li><li>Decontamination</li><li>Premium products</li><li>Attention to detail for a perfect finish</li></ul></div>
    </div>
  </article>

  <article class="panel panel--services-a">
    <h2 class="section-title">Services</h2>
    <div class="service" style="margin-top:14px">
      <div class="photo photo--polish" role="img" aria-label="Polishing machine on car paint"></div>
      <div><h3 class="service-title">Polishing</h3>
        <ul><li>Eliminates scratches, holograms</li><li>Revives and protects paint</li><li>Ensures lasting gloss</li><li>Enhances paint life</li><li>Preserves car’s value and beauty</li></ul></div>
    </div>
    <div class="service">
      <div class="photo photo--car" role="img" aria-label="Water beading on ceramic coated paint"></div>
      <div><h3 class="service-title">Ceramic treatment</h3>
        <ul><li>Durable paint protection</li><li>Water-repellent (hydrophobic) effect</li><li>Easier cleaning, enhanced shine</li><li>Long-term surface safeguarding</li><li>Shields against environmental impacts</li></ul></div>
    </div>
    <div class="service">
      <div class="photo photo--interior" role="img" aria-label="Dry ice cleaning of an engine bay"></div>
      <div><h3 class="service-title">Dry ice wash</h3>
        <ul><li>Innovative, waterless method</li><li>Safe for all car parts</li><li>Deep cleans, removes odors</li><li>Allergen-free, antibacterial</li><li>Gentle, effective</li><li>Advanced cleaning technology</li></ul></div>
    </div>
    <svg class="swoosh" style="left:0;bottom:0" width="254" height="90" viewBox="0 0 254 90"><path d="M0 90 C90 40 170 80 254 30 L254 90Z" fill="var(--violet)" opacity=".4"/></svg>
  </article>

  <article class="panel panel--services-b">
    <div class="service" style="margin-top:6px">
      <div class="photo photo--car" role="img" aria-label="Car being wrapped in coloured vinyl film"></div>
      <div><h3 class="service-title">Covering</h3>
        <ul><li>Personalized vehicle styling</li><li>More than 150 colours available</li><li>Clean cut without using a cutter</li><li>High-quality, durable materials</li><li>Custom designs available</li></ul></div>
    </div>
    <div class="service">
      <div class="photo photo--polish" role="img" aria-label="Clear protection film applied to a bumper"></div>
      <div><h3 class="service-title">Protection film</h3>
        <ul><li>Invisible, durable shield</li><li>Self-healing technology</li><li>10-year warranty by QR VONT</li></ul></div>
    </div>
    <div class="service">
      <div class="photo photo--bottle" role="img" aria-label="Shelf of car care products in the boutique"></div>
      <div><h3 class="service-title">Detailing boutique</h3>
        <ul><li>Premium brands available</li><li>Buy on site during your visit</li><li>Marble Harbour, Zeb Autos, DRUP Polaro</li><li>Essential for at-home car care</li><li>Perfect for quick touch-ups</li></ul></div>
    </div>
    <svg class="swoosh" style="left:0;bottom:0" width="254" height="130" viewBox="0 0 254 130"><path d="M0 130 C70 60 170 110 254 20 L254 130Z" fill="var(--magenta)" opacity=".55"/><path d="M0 130 C90 95 180 125 254 80 L254 130Z" fill="var(--blue)" opacity=".55"/></svg>
  </article>
</section>

</body>
</html>
```